Analytics software company needs a business card design

We need a business card design for a global analytics software provider called 'Varnel Software'. Our main focus is developing real estate analysis software. We are open to any color scheme. The final design should be simple, modern, and precise.
Updates

There is one day left in our project and we are still looking forward to receiving additional submissions. We look forward to selecting one of your designs. Thanks.

Industry/Entity Type

Real Estate

```html
<!DOCTYPE html>
<html lang="en">
<head>
<meta charset="utf-8">
<title>Varnel Software – Business Card</title>
<link href="https://fonts.googleapis.com/css2?family=Open+Sans:wght@400&display=swap" rel="stylesheet">
<style>
  :root {
    --page-bg: #d8d3cb;
    --card-black: #050505;
    --card-light: #c2c2c2;
    --band-dark: #3d3d3d;
    --band-mid: #6a6a6a;
    --band-light: #a3a3a3;
    --text-muted: #8c8c8c;
    --brand-grey: #5e5e5e;
    --shadow: rgba(0, 0, 0, 0.35);
  }
  html, body {
    margin: 0;
    padding: 0;
    width: 1200px;
    height: 1023px;
    overflow: hidden;
    background: var(--page-bg);
    font-family: "Open Sans", sans-serif;
  }
  .canvas {
    position: relative;
    width: 1200px;
    height: 1023px;
  }
  .card {
    position: absolute;
    top: 361px;
    width: 525px;
    height: 300px;
    overflow: hidden;
    box-shadow: 0 10px 24px var(--shadow);
  }
  .card--front {
    left: 50px;
    background: var(--card-black);
  }
  .card--back {
    left: 625px;
    background: var(--card-light);
    display: flex;
    align-items: center;
    justify-content: center;
  }
  .card__swoosh {
    position: absolute;
    inset: 0;
    width: 100%;
    height: 100%;
  }
  .contact {
    position: absolute;
    top: 34px;
    right: 120px;
    margin: 0;
    text-align: right;
    color: var(--text-muted);
    font-size: 15px;
    line-height: 26px;
    list-style: none;
    padding: 0;
  }
  .brand {
    margin: 0;
    font-weight: 400;
    color: var(--brand-grey);
    white-space: nowrap;
  }
  .card--front .brand {
    position: absolute;
    left: 30px;
    bottom: 34px;
    font-size: 30px;
    color: var(--text-muted);
  }
  .card--back .brand {
    font-size: 40px;
  }
</style>
</head>
<body>
<main class="canvas">
  <section class="card card--front" aria-label="Business card front">
    <svg class="card__swoosh" viewBox="0 0 525 300" aria-hidden="true">
      <path d="M150 300 C330 262 430 150 440 0 L525 0 L525 300 Z" fill="var(--band-dark)"/>
      <path d="M255 300 C400 240 468 140 472 0 L525 0 L525 300 Z" fill="var(--band-mid)"/>
      <path d="M345 300 C452 232 500 130 505 0 L525 0 L525 300 Z" fill="var(--band-light)"/>
    </svg>
    <ul class="contact">
      <li>Name</li>
      <li>Position</li>
      <li>Address</li>
      <li>Tel: 555.555.5555</li>
      <li>Email: varnelsoftware@info.com</li>
    </ul>
    <p class="brand">Varnel Software</p>
  </section>

  <section class="card card--back" aria-label="Business card back">
    <p class="brand">Varnel Software</p>
  </section>
</main>
</body>
</html>
```